Clean, minimal label design needed for new skincare line.

Want clean, minimal labels for Clean (non-toxic), cosmeceutical grade Australian-made skincare products. We are going for a minimal and simple approach to our branding so want the labelling to follow suit. Please find logos attached below. Labels are white and logo is black. Font to be black, avoid colours other than white or black.

Target Market(s)

25-65+

Industry/Entity Type

Beauty

Requirements
Must have
• On the front:
- logo
- product name eg. moisturiser 1
- descriptive words eg. light
- weight eg. 30mls/1 fl oz

On the back:
- directions eg. apply one pump both AM and PM after serum application and prior to barrier protect application.
- Cruelty free icon
- Vegan icon
- Made in Australia Icon
- Open jar with 12M Icon
Nice to have
• See above
Should not have
• Avoid colours other than white or black.

```html
<!DOCTYPE html>
<html lang="en">
<head>
<meta charset="utf-8">
<title>Moisturiser 1 Light – Front Label</title>
<link rel="stylesheet" href="https://fonts.googleapis.com/css2?family=Josefin+Sans:wght@600&family=Oswald:wght@500&display=swap">
<style>
  :root {
    --ink: #111111;
    --paper: #ffffff;
    --label-light: #f7f8f9;
    --label-mid: #e4e7e9;
  }
  * { box-sizing: border-box; margin: 0; padding: 0; }
  html, body {
    width: 1200px;
    height: 1092px;
    overflow: hidden;
    background: var(--paper);
  }
  .canvas {
    position: relative;
    width: 1200px;
    height: 1092px;
    background: var(--paper);
  }
  .label {
    position: absolute;
    left: 257px;
    top: 442px;
    width: 722px;
    height: 350px;
    background: linear-gradient(90deg, var(--label-mid) 0%, var(--label-light) 30%, var(--paper) 55%, var(--label-light) 78%, var(--label-mid) 100%);
  }
  .rule {
    position: absolute;
    left: 0;
    right: 0;
    background: var(--ink);
  }
  .rule--top-thin { top: 4px; height: 4px; }
  .rule--top-thick { top: 19px; height: 10px; }
  .rule--bottom-thick { bottom: 19px; height: 10px; }
  .rule--bottom-thin { bottom: 4px; height: 4px; }

  .brand {
    position: absolute;
    left: 28px;
    top: 160px;
    display: flex;
    align-items: center;
    gap: 12px;
  }
  .brand-square {
    width: 16px;
    height: 16px;
    background: var(--ink);
  }
  .brand-name {
    font-family: "Josefin Sans", sans-serif;
    font-weight: 600;
    font-size: 40px;
    line-height: 1;
    color: var(--ink);
    padding-top: 6px;
  }

  .product-name,
  .product-descriptor,
  .product-volume {
    position: absolute;
    right: 28px;
    text-align: right;
    color: var(--ink);
    white-space: nowrap;
    line-height: 1;
  }
  .product-name {
    top: 114px;
    font-family: "Josefin Sans", sans-serif;
    font-weight: 600;
    font-size: 53px;
    letter-spacing: 0.4px;
  }
  .product-descriptor {
    top: 180px;
    font-family: "Josefin Sans", sans-serif;
    font-weight: 600;
    font-size: 39px;
  }
  .product-volume {
    top: 273px;
    font-family: "Oswald", sans-serif;
    font-weight: 500;
    font-size: 22px;
  }
</style>
</head>
<body>
  <main class="canvas">
    <section class="label" aria-label="Front label">
      <div class="rule rule--top-thin"></div>
      <div class="rule rule--top-thick"></div>

      <div class="brand">
        <span class="brand-square"></span>
        <span class="brand-name">Norvale</span>
      </div>

      <h1 class="product-name">MOISTURISER 1</h1>
      <p class="product-descriptor">LIGHT</p>
      <p class="product-volume">30mls/1 fl oz</p>

      <div class="rule rule--bottom-thick"></div>
      <div class="rule rule--bottom-thin"></div>
    </section>
  </main>
</body>
</html>
```